Email Signatures

I would like to create a new email signature for my team. The design will be the same for everyone, with only individual details such as name and email changing. You can also see our brand style on our website. https://www.tlmbespokehomes.com.au/

Target Market(s)

Clients for new builds or renovations

Industry/Entity Type

Construction

Colors

Designer to choose colors to be used in the design.

```html
<!DOCTYPE html>
<html lang="en">
<head>
<meta charset="utf-8">
<title>TLM Bespoke Homes – Email Signature</title>
<link rel="stylesheet" href="https://fonts.googleapis.com/css2?family=Montserrat:wght@400;500;600;700&display=swap">
<style>
  :root {
    --backdrop: #d4d4d4;
    --card: #ffffff;
    --charcoal: #1a1a1a;
    --brand-green: #0b9444;
    --ink: #222222;
    --ink-soft: #3a3a3a;
    --logo-text: #f2f2f2;
  }
  * { margin: 0; padding: 0; box-sizing: border-box; }
  html, body {
    width: 1200px; height: 1200px; overflow: hidden;
    background: var(--backdrop);
    font-family: "Montserrat", Arial, sans-serif;
  }
  .signature {
    position: absolute; left: 58px; top: 449px;
    width: 1100px; height: 302px;
    background: var(--card);
    box-shadow: 0 4px 8px rgba(0,0,0,0.18);
    overflow: hidden;
  }
  .brand-panel { position: absolute; left: 0; top: 0; width: 1100px; height: 302px; }
  .brand-name {
    position: absolute; left: 0; width: 486px; top: 126px;
    text-align: center;
    color: var(--logo-text);
    font-weight: 600; font-size: 32px; letter-spacing: 0.5px;
  }
  .details { position: absolute; left: 601px; top: 0; }
  .person-name {
    position: absolute; top: 55px; white-space: nowrap;
    color: var(--brand-green); font-weight: 700; font-size: 45px;
    letter-spacing: 1.5px; line-height: 1;
  }
  .person-role {
    position: absolute; top: 98px; white-space: nowrap;
    color: var(--ink-soft); font-weight: 400; font-size: 26px; line-height: 1;
  }
  .person-role .divider { font-weight: 300; margin: 0 4px; }
  .rule {
    position: absolute; top: 133px; left: 3px;
    width: 54px; height: 3px; background: var(--brand-green);
  }
  .contact {
    position: absolute; left: 2px; display: flex; align-items: center;
    white-space: nowrap; color: var(--ink); font-size: 27px; line-height: 1;
  }
  .contact svg { width: 25px; height: 25px; margin-right: 11px; flex: none; }
  .contact-phone { top: 160px; }
  .contact-email { top: 199px; }
  .contact-web { top: 237px; }
</style>
</head>
<body>
  <div class="signature">
    <svg class="brand-panel" viewBox="0 0 1100 302" aria-hidden="true">
      <path d="M0 0 H459 Q519 151 459 302 H0 Z" fill="var(--charcoal)"/>
      <path d="M470 -2 Q532 151 470 304" fill="none" stroke="var(--brand-green)" stroke-width="10"/>
    </svg>
    <div class="brand-name">TLM Bespoke Homes</div>

    <div class="details">
      <div class="person-name">FULL NAME</div>
      <div class="person-role">CEO<span class="divider">|</span>Founder</div>
      <div class="rule"></div>

      <div class="contact contact-phone">
        <svg viewBox="0 0 24 24" aria-hidden="true"><path fill="var(--brand-green)" d="M6.6 10.8c1.4 2.8 3.8 5.1 6.6 6.6l2.2-2.2c.3-.3.7-.4 1-.2 1.1.4 2.3.6 3.6.6.6 0 1 .4 1 1V20c0 .6-.4 1-1 1C10.6 21 3 13.4 3 4c0-.6.4-1 1-1h3.5c.6 0 1 .4 1 1 0 1.3.2 2.5.6 3.6.1.3 0 .7-.2 1l-2.3 2.2z"/></svg>
        <span>897-555-0142</span>
      </div>
      <div class="contact contact-email">
        <svg viewBox="0 0 24 24" aria-hidden="true"><rect x="2" y="5" width="20" height="14" fill="var(--brand-green)"/><path d="M2 5 L12 13 L22 5 M2 19 L9.5 11 M22 19 L14.5 11" fill="none" stroke="#fff" stroke-width="1.6"/></svg>
        <span>info@tlmbespokehomes.com.au</span>
      </div>
      <div class="contact contact-web">
        <svg viewBox="0 0 24 24" aria-hidden="true"><g fill="none" stroke="var(--brand-green)" stroke-width="1.6"><circle cx="12" cy="12" r="9.5"/><ellipse cx="12" cy="12" rx="4.5" ry="9.5"/><path d="M12 2.5v19M2.5 12h19M4 7h16M4 17h16"/></g></svg>
        <span>www.tlmbespokehomes.com.au</span>
      </div>
    </div>
  </div>
</body>
</html>
```